Real Estate Investing company needs a business card design

We need a business card design for new Real Estate Investment Company called "Brightgate Holdings, LLC." We buy homes for cash and close quickly in any situation. Our company provides an easy and fast option for home owners who are in tough situations who need to sell their home fast and don't want realtor fees or other listing hassles. We also renovate and resell our homes which helps provide housing for the community. We would like to see designs that use the colors blue and white to match our company logo or other colors that may match our company logo. The final design should communicate trust and easy process.
Industry/Entity Type
Business
Contact Information for Business Card
Front should have company name and company logo. back of card should have company logo and area to list services.
Look and feel

```html
<!DOCTYPE html>
<html lang="en">
<head>
<meta charset="utf-8">
<title>Brightgate Holdings, LLC — Business Card</title>
<link href="https://fonts.googleapis.com/css2?family=Tinos:wght@400;700&display=swap" rel="stylesheet">
<style>
  :root{
    --backdrop:#2c2d31;
    --card-black:#050505;
    --brand-blue:#1474c0;
    --white:#ffffff;
    --soft-white:#e9eef4;
  }
  *{box-sizing:border-box;margin:0;padding:0}
  html,body{width:1200px;height:900px;overflow:hidden}
  body{background:var(--backdrop);font-family:"Tinos","Times New Roman",serif;color:var(--white);position:relative}

  .card{position:absolute;border-radius:26px;overflow:hidden;box-shadow:0 18px 40px rgba(0,0,0,.45)}

  /* Front card (portrait) */
  .card-front{left:110px;top:160px;width:330px;height:580px;background:var(--brand-blue)}
  .front-top{height:270px;background:var(--card-black);display:flex;align-items:center;justify-content:center}
  .brand-name{display:flex;align-items:center;gap:10px;font-weight:700;color:var(--white);text-align:center;line-height:1.1}
  .brand-mark{width:12px;height:12px;background:var(--brand-blue);flex:none}
  .card-front .brand-name{font-size:26px;max-width:260px}

  .contact-list{list-style:none;padding:34px 30px 0 34px}
  .contact-item{display:flex;align-items:center;gap:16px;margin-bottom:24px}
  .contact-icon{width:40px;height:40px;border:2px solid var(--white);border-radius:50%;display:flex;align-items:center;justify-content:center;flex:none}
  .contact-icon svg{width:20px;height:20px;fill:var(--white)}
  .contact-text{font-size:15px;line-height:1.3}
  .contact-text .person{font-weight:700;font-size:18px;letter-spacing:.5px;text-transform:uppercase}
  .contact-text .role{color:var(--soft-white)}
  .contact-text .strong{font-weight:700}

  /* Back card (landscape) */
  .card-back{left:520px;top:280px;width:600px;height:345px;background:var(--card-black)}
  .card-back .brand-name{position:absolute;left:230px;top:60px;font-size:36px;max-width:340px;text-align:left}
  .services{position:absolute;list-style:none;font-size:17px}
  .services li{display:flex;align-items:center;gap:10px;margin-bottom:16px}
  .services-left{left:40px;top:70px}
  .services-right{left:260px;top:205px}
  .window-bullet{width:16px;height:16px;flex:none}
  .window-bullet rect{fill:var(--white)}
</style>
</head>
<body>

<section class="card card-front" aria-label="Business card front">
  <div class="front-top">
    <div class="brand-name"><span class="brand-mark"></span><span>Brightgate Holdings, LLC</span></div>
  </div>
  <ul class="contact-list">
    <li class="contact-item">
      <span class="contact-icon"><svg viewBox="0 0 20 20"><circle cx="10" cy="6" r="4"/><path d="M2 19c0-5 3.5-7 8-7s8 2 8 7z"/></svg></span>
      <div class="contact-text"><div class="person">Daniel Hartley</div><div class="role">Founder &amp; CEO</div></div>
    </li>
    <li class="contact-item">
      <span class="contact-icon"><svg viewBox="0 0 20 20"><path d="M5 2l3 4-2 2c1 2.5 3.5 5 6 6l2-2 4 3-2 3C9 18 2 11 2 4z"/></svg></span>
      <div class="contact-text strong">+1 555 014 2290<br>+1 555 014 2291</div>
    </li>
    <li class="contact-item">
      <span class="contact-icon"><svg viewBox="0 0 20 20" fill="none" stroke="#fff" stroke-width="1.6"><circle cx="10" cy="10" r="8"/><ellipse cx="10" cy="10" rx="3.5" ry="8"/><path d="M2 10h16M3.5 5.5h13M3.5 14.5h13"/></svg></span>
      <div class="contact-text strong">hartley@brightgatehq.com<br>www.brightgatehq.com</div>
    </li>
    <li class="contact-item">
      <span class="contact-icon"><svg viewBox="0 0 20 20"><path d="M10 2l8 7h-2.5v8h-4v-5h-3v5h-4V9H2z"/></svg></span>
      <div class="contact-text">#48, Harbor Lane,<br>Easton-204518</div>
    </li>
  </ul>
</section>

<section class="card card-back" aria-label="Business card back">
  <div class="brand-name"><span class="brand-mark"></span><span>Brightgate Holdings, LLC</span></div>
  <ul class="services services-left">
    <li><svg class="window-bullet" viewBox="0 0 16 16"><rect x="0" y="0" width="7" height="7"/><rect x="9" y="0" width="7" height="7"/><rect x="0" y="9" width="7" height="7"/><rect x="9" y="9" width="7" height="7"/></svg>Property Acquisition</li>
    <li><svg class="window-bullet" viewBox="0 0 16 16"><rect x="0" y="0" width="7" height="7"/><rect x="9" y="0" width="7" height="7"/><rect x="0" y="9" width="7" height="7"/><rect x="9" y="9" width="7" height="7"/></svg>Property Rehabilitation</li>
  </ul>
  <ul class="services services-right">
    <li><svg class="window-bullet" viewBox="0 0 16 16"><rect x="0" y="0" width="7" height="7"/><rect x="9" y="0" width="7" height="7"/><rect x="0" y="9" width="7" height="7"/><rect x="9" y="9" width="7" height="7"/></svg>Property Financing and closing</li>
    <li><svg class="window-bullet" viewBox="0 0 16 16"><rect x="0" y="0" width="7" height="7"/><rect x="9" y="0" width="7" height="7"/><rect x="0" y="9" width="7" height="7"/><rect x="9" y="9" width="7" height="7"/></svg>Property Management</li>
  </ul>
</section>

</body>
</html>
```